I need a cover designed for a leadership book to fit my brand of my podcast, Ask the Dispensary Desk, www.dosageharborhub.com, with blues and greens and a professional look since it will be for a professional audience of pharmacists.

Some ideas for an image for the cover might be a woman's hand holding a compass with a road, but I welcome other ideas.

Title of the book is
"Where Chemists Steer: Voices from Women [on the Rise] Who Are Guiding, Thriving, and Reshaping Dispensing"

```html
<!DOCTYPE html>
<html lang="en">
<head>
<meta charset="utf-8">
<title>Where Chemists Steer — Book Cover</title>
<link rel="stylesheet" href="https://fonts.googleapis.com/css2?family=Anton&family=Montserrat:wght@500&display=swap">
<style>
  :root {
    --navy-deep: #161a55;
    --navy-glow: #28368f;
    --lime: #74d420;
    --ink: #181a4c;
    --white: #ffffff;
    --brass-light: #f3e3b6;
    --brass-mid: #c9a25a;
    --brass-dark: #6d4a1d;
  }
  * { margin: 0; padding: 0; box-sizing: border-box; }
  html, body { width: 886px; height: 1200px; overflow: hidden; background: var(--ink); }
  .cover {
    position: relative;
    width: 886px;
    height: 1200px;
    overflow: hidden;
    background: var(--lime);
  }
  .cover__top {
    position: absolute;
    left: 0; top: 0;
    width: 100%;
    height: 758px;
    background: radial-gradient(ellipse 70% 60% at 50% 42%, var(--navy-glow), var(--navy-deep) 80%);
  }
  .title {
    position: absolute;
    inset: 0;
    font-family: 'Anton', 'Impact', sans-serif;
    font-weight: 400;
    text-transform: uppercase;
  }
  .title__line {
    position: absolute;
    display: block;
    line-height: 1;
    white-space: nowrap;
  }
  .title__lead-in {
    left: 112px;
    color: var(--lime);
  }
  .title__lead-in--first { top: 66px; font-size: 112px; }
  .title__lead-in--second { top: 182px; font-size: 140px; }
  .title__main {
    left: 0; width: 100%;
    top: 319px;
    text-align: center;
    color: var(--white);
    font-size: 315px;
    letter-spacing: -3px;
    transform-origin: center top;
    transform: scaleY(1.3);
  }
  .compass {
    position: absolute;
    left: 355px; top: 655px;
    width: 210px; height: 210px;
    border-radius: 50%;
    background: radial-gradient(circle at 45% 40%, var(--brass-light) 0 48%, var(--brass-mid) 62%, var(--brass-dark) 100%);
    box-shadow: 0 8px 18px rgba(0,0,0,0.35);
  }
  .subtitle {
    position: absolute;
    left: 60px; right: 60px;
    top: 884px;
    text-align: center;
    font-family: 'Montserrat', 'Arial', sans-serif;
    font-weight: 500;
    font-size: 31px;
    line-height: 1.38;
    color: var(--ink);
  }
  .author {
    position: absolute;
    left: 0; width: 100%;
    top: 1062px;
    text-align: center;
    font-family: 'Anton', 'Impact', sans-serif;
    font-size: 58px;
    line-height: 1;
    color: var(--ink);
    text-transform: uppercase;
    transform-origin: center top;
    transform: scaleY(1.2);
  }
</style>
</head>
<body>
  <main class="cover">
    <div class="cover__top"></div>
    <h1 class="title">
      <span class="title__line title__lead-in title__lead-in--first">Where</span>
      <span class="title__line title__lead-in title__lead-in--second">Chemists</span>
      <span class="title__line title__main">Steer</span>
    </h1>
    <div class="compass" role="img" aria-label="Brass navigation compass illustration"></div>
    <p class="subtitle">Voices from Women [on the Rise]<br>Who Are Guiding, Thriving, and<br>Reshaping Dispensing</p>
    <p class="author">Dr. Marlowe Ashcroft, PharmD</p>
  </main>
</body>
</html>
```